BQN Project Signage

Need a sign to be displayed in the front of properties currently under Construction or Renovation to advertise our company information. Need it to be Professional and Contemporary. We are a Design/Build Construction Company. Information should include Company Name, email, website, phone number. Attached: Logo and company brochure, also included and inspiration images

```html
<!DOCTYPE html>
<html lang="en">
<head>
<meta charset="utf-8">
<title>BQN Construction – Project Sign</title>
<link rel="stylesheet" href="https://fonts.googleapis.com/css2?family=Figtree:wght@700;800&display=swap">
<style>
  :root {
    --backdrop: #cccccc;
    --sign-white: #ffffff;
    --sign-black: #000000;
    --icon-grey: #b3b3b3;
    --text-light: #efefef;
  }
  * { margin: 0; padding: 0; box-sizing: border-box; }
  html, body {
    width: 1139px;
    height: 1200px;
    overflow: hidden;
    background: var(--backdrop);
    font-family: "Figtree", "Helvetica Neue", Arial, sans-serif;
  }
  .sign {
    position: absolute;
    left: 270px;
    top: 117px;
    width: 635px;
    height: 948px;
    background: var(--sign-white);
    overflow: hidden;
  }
  .brand-name {
    position: absolute;
    left: 0;
    width: 606px;
    top: 106px;
    text-align: center;
    font-size: 42px;
    font-weight: 700;
    letter-spacing: 1px;
    line-height: 1;
    color: var(--sign-black);
  }
  .brand-tagline {
    position: absolute;
    left: 0;
    width: 606px;
    top: 162px;
    text-align: center;
    font-size: 21px;
    font-weight: 700;
    letter-spacing: 2px;
    line-height: 1;
    color: var(--sign-black);
  }
  .contact-band {
    position: absolute;
    left: 0;
    top: 331px;
    width: 635px;
    height: 509px;
    background: var(--sign-black);
  }
  .service-pill {
    position: absolute;
    left: 56px;
    top: 293px;
    width: 527px;
    height: 83px;
    border: 4px solid var(--sign-black);
    border-radius: 42px;
    background: var(--sign-white);
    display: flex;
    align-items: center;
    justify-content: center;
    padding-left: 36px;
    font-size: 52px;
    font-weight: 800;
    color: var(--sign-black);
  }
  .contact-icon {
    position: absolute;
    width: 50px;
    height: 50px;
    left: 297px;
  }
  .contact-text {
    position: absolute;
    left: 0;
    width: 635px;
    text-align: center;
    font-weight: 700;
    font-style: normal;
    color: var(--text-light);
    line-height: 1;
  }
  .contact-phone { top: 456px; font-size: 43px; letter-spacing: 1px; }
  .contact-email { top: 578px; font-size: 31px; }
  .contact-address { top: 696px; font-size: 33px; line-height: 37px; }
  .website {
    position: absolute;
    left: 0;
    width: 635px;
    top: 876px;
    text-align: center;
    font-size: 37px;
    font-weight: 800;
    line-height: 1;
    color: var(--sign-black);
  }
</style>
</head>
<body>
  <main class="sign">
    <h1 class="brand-name">BQN CONSTRUCTION</h1>
    <p class="brand-tagline">LUXURY RENOVATIONS</p>

    <section class="contact-band"></section>
    <div class="service-pill">DESIGN - BUILD</div>

    <svg class="contact-icon" style="top:397px" viewBox="0 0 50 50" aria-hidden="true">
      <circle cx="25" cy="25" r="25" fill="var(--icon-grey)"/>
      <path d="M15 12 l5 -2 l4 8 l-3 3 q2 6 7 9 l3 -3 l8 4 l-2 5 q-6 3 -14 -5 q-9 -10 -8 -19z" fill="var(--sign-black)"/>
      <path d="M29 16 a6 6 0 0 1 5 5 M30 11 a11 11 0 0 1 9 9" stroke="var(--sign-black)" stroke-width="1.8" fill="none" stroke-linecap="round"/>
    </svg>
    <p class="contact-text contact-phone">555.014.2273</p>

    <svg class="contact-icon" style="top:518px" viewBox="0 0 50 50" aria-hidden="true">
      <circle cx="25" cy="25" r="25" fill="var(--icon-grey)"/>
      <rect x="11" y="15" width="28" height="20" fill="none" stroke="var(--sign-black)" stroke-width="2.2"/>
      <path d="M11 15 l14 12 l14 -12 M11 35 l10 -10 M39 35 l-10 -10" fill="none" stroke="var(--sign-black)" stroke-width="2"/>
    </svg>
    <p class="contact-text contact-email">info@bqnconstruction.com</p>

    <svg class="contact-icon" style="top:637px" viewBox="0 0 50 50" aria-hidden="true">
      <circle cx="25" cy="25" r="25" fill="var(--icon-grey)"/>
      <path d="M25 40 q-11 -12 -11 -19 a11 11 0 0 1 22 0 q0 7 -11 19z" fill="none" stroke="var(--sign-black)" stroke-width="2"/>
      <circle cx="25" cy="21" r="4.5" fill="none" stroke="var(--sign-black)" stroke-width="2"/>
    </svg>
    <address class="contact-text contact-address">
      4180 Harbor View Rd.<br>Suite 310<br>Coral Ridge, FL 33400
    </address>

    <p class="website">www.bqnconstruction.com</p>
  </main>
</body>
</html>
```